Webdesign für Maklerbüro
Zielgruppe
Wir sind ein Maklerbüro aus Nürnberg, das sich auf den Verkauf von Eigentumswohnungen und Häuser spezialisiert hat. Mit der neuen Seite möchten wir vor allem Eigentümer ansprechen und über unsere Arbeitsweise informieren. Der Hauptzweck ist damit die Akquise von neuen Objekten, für die Vermittlung. Die Zielgruppe sind vornehmlich Immobilienbesitzer im Alter 40+ und im gehobenen Preissegment.
Aufgabenstellung
Beim Design bitte an den Vorgaben des Logo (Datei beigefügt) orientieren. Bilder und Texte können durch 'Platzhalter' ersetzt werden.
Grundsätzlich stellt es für uns kein Problem dar, sich an Template-Vorlagen zu orientieren. Wir stellen uns eine Seite mit Pfiff und Ideenreichtum – einfach weg vom Standard – vor. Wir verkaufen Immobilien, aber vom verstaubten Krawattenträger sind wir weit entfernt. Wir sind ein junges Unternehmen, das neue Marketingwege beschreitet. Unsere Webseite muss das ausdrücken. Kein Standard, und damit auch keine Standard-Webseite. Designs, die uns gut gefallen (und in die Richtung es auch gehen kann) haben wir beigefügt.

```html
<!DOCTYPE html>
<html lang="de">
<head>
<meta charset="utf-8">
<title>Hausfranken – Immobilienmakler Nürnberg</title>
<link href="https://fonts.googleapis.com/css2?family=Open+Sans:wght@600;700&family=Source+Sans+3:ital,wght@0,400;0,600;0,700;1,400&display=swap" rel="stylesheet">
<style>
:root{
  --navy:#141c3a;
  --navy-soft:#1b2549;
  --paper:#f2f2f2;
  --accent:#5a76c9;
  --stripe:#1c8fd6;
  --ink:#1a2345;
  --white:#ffffff;
}
*{box-sizing:border-box;margin:0;padding:0}
html,body{width:1200px;height:2855px;overflow:hidden}
body{background:var(--paper);font-family:"Source Sans 3",Arial,sans-serif;color:var(--ink);position:relative}
.abs{position:absolute}
.shapes{position:absolute;left:0;top:0}
.nav-bar{left:0;top:80px;width:1100px;height:43px;background:var(--navy);opacity:.92}
.brand{left:114px;top:82px;font-size:34px;font-weight:600;color:var(--white);letter-spacing:1px;line-height:40px}
.menu{left:1058px;top:88px;width:34px}
.menu span{display:block;height:4px;background:var(--white);margin-bottom:6px}
.hero-title{left:0;width:1200px;top:288px;text-align:center;font-family:"Open Sans",Arial,sans-serif;font-weight:700;font-size:28px;color:var(--white);text-shadow:0 1px 6px rgba(0,0,0,.35)}
.btn{position:absolute;border:4px solid var(--accent);display:flex;align-items:center;justify-content:center;font-size:26px;background:transparent}
.btn-hero{left:460px;top:431px;width:276px;height:48px;color:var(--white);font-family:"Open Sans",Arial,sans-serif;font-weight:700;font-size:24px}
.section-title{left:0;width:1200px;text-align:center;font-size:33px;font-weight:400;color:var(--ink)}
.intro{left:111px;top:682px;width:975px;font-size:13.3px;line-height:26.4px;text-align:justify;color:var(--ink)}
.valuation-title{left:132px;top:962px;font-size:25px;font-weight:700;color:var(--white)}
.valuation-sub{left:215px;top:998px;font-size:17px;color:var(--white)}
.btn-valuation{left:783px;top:966px;width:222px;height:48px;color:var(--white);font-size:24px}
.service-card{position:absolute;top:1208px;width:193px;height:261px;background:var(--navy);color:var(--white);text-align:center}
.service-card svg{margin-top:38px}
.service-card h3{font-size:20px;font-weight:400;margin-top:12px}
.service-card p{font-size:11px;line-height:14px;text-align:left;padding:0 26px;margin-top:16px}
.arrow{position:absolute;top:1322px;width:37px;height:37px;border-radius:50%;background:var(--navy);color:var(--white);font-size:22px;display:flex;align-items:center;justify-content:center;line-height:1}
.btn-appointment{left:464px;top:1499px;width:267px;height:49px;color:var(--ink);font-size:26px}
.reviews-title{color:var(--white)}
.quote-mark{left:111px;top:1740px}
.review{left:250px;top:1740px;width:750px;font-size:16.5px;line-height:26.5px;color:var(--white);text-align:justify}
.review-author{left:750px;width:250px;top:1818px;text-align:right;font-style:italic;font-size:14px;color:#8a93ad}
.dots{left:566px;top:1892px;display:flex;gap:7px}
.dots span{width:16px;height:16px;border-radius:50%;background:#c9ccd6}
.dots span:first-child{background:#2a4ba0}
.contact-row{position:absolute;left:111px;display:flex;align-items:center}
.contact-row .icon{width:46px;display:flex;justify-content:center}
.contact-row p{margin-left:38px;font-size:16px;line-height:27px;color:var(--ink)}
.field{position:absolute;background:var(--navy);border-right:6px solid var(--stripe);color:var(--white);font-size:15px;padding:8px 16px}
.btn-send{left:529px;top:2685px;width:576px;height:48px;color:var(--ink);font-size:26px}
.footer{left:0;top:2811px;width:1200px;height:44px;background:var(--navy);display:flex;justify-content:center;gap:56px;align-items:center;color:var(--white);font-size:17px}
</style>
</head>
<body>

<svg class="shapes" width="1200" height="2855" viewBox="0 0 1200 2855" aria-hidden="true">
  <defs>
    <linearGradient id="dusk" x1="0" y1="0" x2="0" y2="1">
      <stop offset="0" stop-color="#5d6b8e"/>
      <stop offset=".45" stop-color="#6f7b92"/>
      <stop offset=".8" stop-color="#4e5567"/>
      <stop offset="1" stop-color="#3b4150"/>
    </linearGradient>
    <linearGradient id="mapTone" x1="0" y1="0" x2="1" y2="0">
      <stop offset="0" stop-color="#e6e3da"/>
      <stop offset=".35" stop-color="#a9cdef"/>
      <stop offset=".6" stop-color="#ece8df"/>
      <stop offset="1" stop-color="#c7dcae"/>
    </linearGradient>
    <filter id="shadow" x="-5%" y="-20%" width="110%" height="140%">
      <feDropShadow dx="0" dy="6" stdDeviation="6" flood-color="#000" flood-opacity=".25"/>
    </filter>
  </defs>
  <!-- dark band: valuation -->
  <polygon points="0,875 600,925 1200,875 1200,1047 600,1097 0,1047" fill="#141c3a" filter="url(#shadow)"/>
  <!-- dark band: reviews -->
  <polygon points="0,1556 600,1604 1200,1556 1200,1940 0,1940" fill="#141c3a"/>
</svg>

<svg class="abs" style="left:0;top:0" width="1200" height="590" viewBox="0 0 1200 590" role="img" aria-label="Foto: Einfamilienhaus mit Garage in der Abenddämmerung">
  <polygon points="0,0 1200,0 1200,541 600,587 0,541" fill="url(#dusk)"/>
</svg>

<svg class="abs" style="left:0;top:1911px" width="1200" height="300" viewBox="0 0 1200 300" role="img" aria-label="Stadtplan mit Lage des Maklerbüros">
  <polygon points="0,0 600,39 1200,0 1200,244 600,294 0,244" fill="url(#mapTone)" filter="url(#shadow)"/>
</svg>

<div class="abs nav-bar"></div>
<div class="abs brand">HAUSFRANKEN</div>
<div class="abs menu"><span></span><span></span><span></span></div>

<h1 class="abs hero-title">Ihr Immobilienmakler für die Metropolregion Nürnberg.</h1>
<a class="btn btn-hero">Wer wir sind.</a>

<h2 class="abs section-title" style="top:616px">Die richtige Wahl des Immobilienmaklers.</h2>
<p class="abs intro">Lorem ipsum dolor sit amet, consectetur adipiscing elit. Sed faucibus libero egestas lorem euismod gravida. Nullam et ultrices ipsum. Cras semper turpis ut pellentesque aliquet. Praesent at pulvinar justo. Duis ultrices pellentesque vestibulum. Integer nec enim ac ligula lobortis dictum. Vestibulum sit amet dolor et mauris fermentum commodo. Proin rhoncus sit amet diam tincidunt sagittis. Quisque fringilla, est a tincidunt mattis, turpis quam convallis sapien, quis pulvinar nulla lacus quis erat. Interdum et malesuada fames ac ante ipsum primis in faucibus. Etiam suscipit convallis cursus. Aliquam lacinia, eros a convallis porta, enim nisl aliquam dolor, sit amet egestas ante mauris et enim. Integer condimentum ligula in ullamcorper cursus. Curabitur mollis semper justo, ac dignissim odio euismod sed. Donec quis mauris at justo aliquam eleifend vel in neque.</p>

<h2 class="abs valuation-title">Professionelle Immobilienbewertung</h2>
<p class="abs valuation-sub">Was ist meine Immobilie Wert? Wir finden den richtigen Preis für Sie.</p>
<a class="btn btn-valuation">Jetzt Anfragen!</a>

<h2 class="abs section-title" style="top:1129px">Rundum Sorglos Vertrieb Ihrer Immobilie.</h2>

<div class="arrow" style="left:75px">&lt;</div>
<div class="arrow" style="left:1086px">&gt;</div>

<div class="service-card" style="left:252px">
  <svg width="80" height="82" viewBox="0 0 80 82" fill="none" stroke="#fff" stroke-width="3" stroke-linejoin="round">
    <path d="M4 42 L40 8 L76 42"/><path d="M14 34 V78 H66 V34"/><path d="M22 22 V8 H30 V15"/>
    <rect x="34" y="52" width="12" height="26"/><rect x="20" y="50" width="10" height="10"/><rect x="50" y="50" width="10" height="10"/><path d="M30 36 H50"/>
  </svg>
  <h3>Objektaufnahme</h3>
  <p>Detallierte Einwertung, Preisfindung, Vermessung und Fotografie Ihrer Immobilie.</p>
</div>

<div class="service-card" style="left:501px">
  <svg width="82" height="76" viewBox="0 0 82 76" fill="none" stroke="#fff" stroke-width="3" stroke-linejoin="round" stroke-linecap="round">
    <path d="M20 30 L41 10 L62 30"/><path d="M27 26 V48 H55 V26"/><rect x="37" y="34" width="8" height="14"/>
    <path d="M4 30 C4 50 14 62 28 66 L34 58 L24 48"/><path d="M78 30 C78 50 68 62 54 66 L48 58 L58 48"/>
  </svg>
  <h3>Vermarktung</h3>
  <p>Gemeinsame Festlegung eines Vermarktungs- &amp; Präsentationskonzeptes für Ihre Immobilie.</p>
</div>

<div class="service-card" style="left:750px">
  <svg width="82" height="76" viewBox="0 0 82 76" fill="none" stroke="#fff" stroke-width="3" stroke-linejoin="round" stroke-linecap="round">
    <path d="M20 30 L41 10 L62 30"/><path d="M27 26 V48 H55 V26"/><rect x="37" y="34" width="8" height="14"/>
    <path d="M4 30 C4 50 14 62 28 66 L34 58 L24 48"/><path d="M78 30 C78 50 68 62 54 66 L48 58 L58 48"/>
  </svg>
  <h3>Präsentation</h3>
  <p>Präsentation in Zeitungen, gängigen Internetportalen und weitere Präsentations­möglichkeiten nach Wunsch.</p>
</div>

<a class="btn btn-appointment">Termin vereinbaren</a>

<h2 class="abs section-title reviews-title" style="top:1657px">Das sagen Unsere Kunden.</h2>
<svg class="abs quote-mark" width="86" height="66" viewBox="0 0 86 66" aria-hidden="true">
  <path d="M0 0 H38 V34 C38 52 28 62 10 66 L6 56 C16 52 20 46 20 38 H0 Z" fill="#8a93ad"/>
  <path d="M48 0 H86 V34 C86 52 76 62 58 66 L54 56 C64 52 68 46 68 38 H48 Z" fill="#8a93ad"/>
</svg>
<p class="abs review">Ich würde Herrn Brennholt als freundlich, zuverlässig und integer beschreiben. Eigenschaften, die in dieser Kombination nicht branchentypisch sind. Er hat uns beim Erwerb einer Eigentumswohnung sehr kompetent beraten und bis zum Abschluss herausragend begleitet. Ich kann die "Lukas Brennholt Immobilienberatung" wirklich uneingeschränkt empfehlen.</p>
<p class="abs review-author">Peter M. (Käufer)</p>
<div class="abs dots"><span></span><span></span><span></span></div>

<h2 class="abs section-title" style="top:2255px">Treten Sie mit Uns in Kontakt.</h2>

<div class="contact-row" style="top:2352px">
  <div class="icon"><svg width="40" height="46" viewBox="0 0 40 46" fill="none" stroke="#1a2345" stroke-width="2"><rect x="4" y="2" width="20" height="42"/><rect x="24" y="18" width="14" height="26"/><path d="M9 8h4M16 8h4M9 15h4M16 15h4M9 22h4M16 22h4M9 29h4M16 29h4M28 24h6M28 31h6M28 38h6"/></svg></div>
  <p>Lindenhof-Straße 24<br>90482 Nürnberg</p>
</div>
<div class="contact-row" style="top:2444px">
  <div class="icon"><svg width="46" height="46" viewBox="0 0 46 46" fill="none" stroke="#1a2345" stroke-width="2" stroke-linejoin="round"><path d="M10 3 L17 13 L12 19 C15 27 20 32 28 35 L33 29 L43 36 L38 43 C20 42 4 26 3 9 Z"/></svg></div>
  <p>+49 911 5550 21 40</p>
</div>
<div class="contact-row" style="top:2530px">
  <div class="icon"><svg width="30" height="46" viewBox="0 0 30 46" fill="none" stroke="#1a2345" stroke-width="2"><rect x="2" y="2" width="26" height="42" rx="4"/><path d="M2 9h26M2 36h26M12 40h6"/></svg></div>
  <p>+49 176 5550 73 92</p>
</div>
<div class="contact-row" style="top:2620px">
  <div class="icon"><svg width="46" height="32" viewBox="0 0 46 32" fill="none" stroke="#1a2345" stroke-width="2" stroke-linejoin="round"><rect x="2" y="2" width="42" height="28"/><path d="M2 2 L23 19 L44 2M2 30 L17 15M44 30 L29 15"/></svg></div>
  <p>kontakt@hausfranken.de</p>
</div>

<div class="field" style="left:529px;top:2355px;width:268px;height:35px">Ihr Name*</div>
<div class="field" style="left:837px;top:2355px;width:268px;height:35px">Straße, Hausnummer*</div>
<div class="field" style="left:529px;top:2408px;width:268px;height:35px">E-Mail*</div>
<div class="field" style="left:837px;top:2408px;width:268px;height:35px">Postleitzahl, Ort*</div>
<div class="field" style="left:529px;top:2466px;width:576px;height:195px;padding-top:12px">Ihre Nachricht an Uns.</div>
<a class="btn btn-send">Senden</a>

<footer class="abs footer"><span>Impressum</span><span>Datenschutz</span></footer>

</body>
</html>
```